Funeral Services Site

We need a website for a Funeral Services company. The old website is: www.rouwcentrumkorvelaer.be We need the same structure and text.

Target Market(s)

Customers.

Coding

Coded - Design and coding required

Number of Pages Required

4 page

Font styles to use
Serif
Sans Serif
Script

```html
<!DOCTYPE html>
<html lang="en">
<head>
<meta charset="utf-8">
<title>Funeral home Verhaegen bvba</title>
<link rel="stylesheet" href="https://fonts.googleapis.com/css2?family=Tinos:wght@400;700&family=Jost:wght@400;500&family=Parisienne&display=swap">
<style>
:root{
  --gold:#a8840f;
  --ink:#1b1b1b;
  --topbar:#2c2c2c;
  --footer:#1a1a1a;
  --bottombar:#343434;
  --panel:#efefef;
  --text:#444;
  --white:#fff;
}
*{box-sizing:border-box;margin:0;padding:0}
html,body{width:1200px;height:3070px;overflow:hidden}
body{font-family:"Jost",sans-serif;color:var(--text);background:var(--white);position:relative}
section,header,footer,.topbar,.bottombar{position:absolute;left:0;width:1200px}

/* top bar */
.topbar{top:0;height:43px;background:var(--topbar);color:#eee}
.topbar .item{position:absolute;top:0;height:43px;display:flex;align-items:center;gap:10px}
.topbar .phone{left:142px;font-size:16px}
.topbar .mail{left:286px;font-size:13px}
.lang{position:absolute;left:1003px;top:5px;width:56px;height:32px;background:#fff;color:var(--gold);font-size:13px;display:flex;align-items:center;justify-content:center;gap:4px}

/* header */
header{top:43px;height:100px;background:#fff}
.brand{position:absolute;left:142px;top:17px;display:flex;align-items:center;gap:12px}
.brand-mark{width:58px;height:58px;border-radius:50%;background:var(--ink)}
.brand-name{font-family:"Tinos",serif;font-weight:700;font-size:23px;line-height:25px;color:var(--ink)}
.brand-name small{font-size:17px}
.nav{position:absolute;right:140px;top:0;height:100px;display:flex}
.nav a{display:flex;align-items:center;padding:0 21px;font-family:"Tinos",serif;font-weight:700;font-size:15px;color:var(--ink);text-decoration:none;position:relative}
.nav a.active{background:#f3f3f3;color:var(--gold);border-bottom:3px solid var(--gold);padding:0 22px}
.nav a.active::after{content:"";position:absolute;left:50%;bottom:0;margin-left:-5px;border:5px solid transparent;border-bottom-color:var(--gold)}

/* hero */
.hero{top:143px;height:548px;background:linear-gradient(100deg,#141210 0%,#2a241c 30%,#6d6148 52%,#a6b07a 70%,#dcd9b4 85%,#c7cf93 100%)}
.hero-title{position:absolute;left:142px;top:168px;font-family:"Parisienne",cursive;font-size:54px;line-height:68px;color:#fff;font-weight:400}
.btn-outline{position:absolute;display:flex;align-items:center;justify-content:center;font-family:"Tinos",serif;font-weight:700;text-decoration:none}
.btn-light{border:2px solid #fff;color:#fff}
.btn-gold{border:2px solid var(--gold);color:var(--gold)}

/* about */
.about{top:691px;height:522px}
.about-frame{position:absolute;left:148px;top:92px;width:367px;height:345px;border:2px solid var(--gold)}
.about-photo{position:absolute;left:141px;top:85px;width:367px;height:345px;background:linear-gradient(135deg,#e8d8b4 0%,#8a5a22 40%,#5a3a1e 65%,#3d2a4a 100%)}
.about-text{position:absolute;left:552px;top:112px;width:510px}
.about-text h2{font-family:"Tinos",serif;font-weight:700;font-size:28px;color:var(--ink)}
.about-text h2 small{font-size:18px}
.about-text h3{font-weight:400;font-size:18px;line-height:25px;color:#222;margin-top:10px}
.about-text p{font-size:13.4px;line-height:22px;margin-top:6px}

/* organisation */
.org{top:1213px;height:619px}
.org-band{position:absolute;left:0;top:0;width:1200px;height:357px;background:linear-gradient(90deg,#2f3325 0%,#2c2c2c 30%,#232323 55%,#3a3a2e 80%,#4a4d38 100%)}
.org h2{position:absolute;top:80px;width:1200px;text-align:center;font-family:"Tinos",serif;font-weight:700;font-size:29px;color:#fff}
.org p{position:absolute;width:1200px;text-align:center;font-size:13.4px;line-height:22px;color:#fff}
.service{position:absolute;top:270px;width:300px;text-align:center}
.service .circle{width:178px;height:178px;margin:0 auto;border-radius:50%;border:6px solid #fff;box-shadow:0 0 0 1px #ddd}
.service h4{font-family:"Tinos",serif;font-weight:700;font-size:19px;line-height:26px;color:#333;margin-top:20px}
.service small{display:block;font-family:"Tinos",serif;font-weight:700;font-size:11px;line-height:16px;color:#444}

/* call to action */
.cta{top:1832px;height:352px;background:linear-gradient(90deg,#3a2c1c 0%,#4a3820 35%,#6a5a48 55%,#cfc6d8 68%,#e8e0cc 80%,#5a6a3e 100%)}
.cta .q{position:absolute;left:142px;top:92px;font-family:"Tinos",serif;font-weight:700;font-size:20px;line-height:30px;color:#fff}
.cta .lead{position:absolute;left:142px;top:152px;font-family:"Tinos",serif;font-weight:700;font-size:28px;color:#fff}
.cta .call{position:absolute;left:315px;top:225px;font-family:"Tinos",serif;font-weight:700;font-size:16px;color:#fff}

/* inquiry */
.inquiry{top:2184px;height:587px}
.inquiry-box{position:absolute;left:275px;top:85px;width:650px;height:420px;background:var(--panel);overflow:hidden}
.inquiry-box h2{position:absolute;top:30px;width:650px;text-align:center;font-family:"Tinos",serif;font-weight:700;font-size:29px;color:var(--ink)}
.inquiry-box .intro{position:absolute;top:70px;width:650px;text-align:center;font-size:13.4px;line-height:21px;color:#444}
.field{position:absolute;background:#fff;border:1px solid #d6d6d6;font-size:13px;color:#555;padding:10px 16px}
.corner{position:absolute;left:0;bottom:0}

/* footer */
footer{top:2771px;height:257px;background:var(--footer);color:#ddd}
footer h5{position:absolute;top:64px;font-family:"Tinos",serif;font-weight:700;font-size:14.5px;color:#fff}
.links{position:absolute;left:142px;top:90px;list-style:none;font-size:12.5px;line-height:25.5px}
.links li::before{content:"»";color:#888;margin-right:10px;font-size:11px}
.contact{position:absolute;left:310px;top:88px;font-size:12.5px;line-height:17px}
.contact .row{display:flex;gap:8px;margin-bottom:10px}
.map{position:absolute;left:596px;top:85px;width:205px;height:110px;background:linear-gradient(135deg,#eef0e8,#d9dfe6)}
.foot-brand{position:absolute;left:866px;top:107px;display:flex;align-items:center;gap:10px}
.foot-brand .brand-mark{width:44px;height:44px;background:#fff}
.foot-brand .brand-name{color:#fff;font-size:17px;line-height:19px}
.foot-brand .brand-name small{font-size:13px}
.social{position:absolute;left:906px;top:150px;display:flex;gap:12px}
.social span{width:18px;height:18px;background:#5b5b5b}

.bottombar{top:3028px;height:42px;background:var(--bottombar);color:#eee;font-size:12.5px}
.bottombar .copy{position:absolute;left:142px;top:13px}
.bottombar .legal{position:absolute;right:140px;top:13px}
</style>
</head>
<body>

<div class="topbar">
  <div class="item phone">
    <svg width="20" height="20" viewBox="0 0 24 24" fill="none" stroke="#eee" stroke-width="1.6"><path d="M5 3h4l2 5-2.5 1.5a11 11 0 0 0 6 6L16 13l5 2v4a2 2 0 0 1-2 2A16 16 0 0 1 3 5a2 2 0 0 1 2-2z"/></svg>
    013 58 20 40
  </div>
  <div class="item mail">
    <svg width="20" height="16" viewBox="0 0 24 18" fill="none" stroke="#eee" stroke-width="1.5"><rect x="1" y="1" width="22" height="16" rx="1"/><path d="M1 2l11 8 11-8"/></svg>
    contact@verhaegen-rouw.example
  </div>
  <div class="lang">EN <svg width="8" height="5" viewBox="0 0 8 5"><path d="M0 0h8L4 5z" fill="#a8840f"/></svg></div>
</div>

<header>
  <div class="brand">
    <span class="brand-mark"></span>
    <div class="brand-name">Funeral home<br>Verhaegen <small>bvba</small></div>
  </div>
  <nav class="nav">
    <a class="active">Home</a>
    <a>About us</a>
    <a>Condole online</a>
    <a>Order flowers</a>
    <a>Contact</a>
  </nav>
</header>

<section class="hero" role="img" aria-label="Photo of a coffin with white roses and green flowers">
  <h1 class="hero-title">A Personal Service In<br>Farewell Guidance</h1>
  <a class="btn-outline btn-light" style="left:142px;top:323px;width:174px;height:46px;font-size:16px">Contact Us Today</a>
</section>

<section class="about">
  <div class="about-frame"></div>
  <div class="about-photo" role="img" aria-label="Photo of a wooden coffin covered with white flowers in a church"></div>
  <div class="about-text">
    <h2>About Funeral Home Verhaegen <small>Bvba</small></h2>
    <h3>Mourning center Verhaegen, a complete service in mourning and farewell guidance</h3>
    <p>Saying goodbye to a loved one is one of the toughest things in a lifetime. Funeral home Verhaegen in Heidewaarde takes care of all the practical and administrative matters involved. So you can say goodbye in peace.</p>
    <p>Our people have a r uime experience in farewell guidance and stand for 24 hours at 24 hours for you. Our fully renovated funeral home is open to you and your acquaintances, so that you can greet your loved one at any time of the day.</p>
  </div>
  <a class="btn-outline btn-gold" style="left:552px;top:363px;width:121px;height:40px;font-size:14px">Read More</a>
</section>

<section class="org">
  <div class="org-band" role="img" aria-label="Photo of a cemetery at dusk with headstones and flowers"></div>
  <h2>Organization Funeral And Worship</h2>
  <p style="top:127px">The organization of the funeral ceremony is a moment of reflection, where the personality of the deceased can be beautifully highlighted. Our team<br>will assist you in this and select the most beautiful texts, songs and photos with you in order to arrive at an appropriate and worthy goodbye.</p>
  <p style="top:182px">The funeral can take place in your parish church or &nbsp;our auditorium if you wish, which can accommodate a maximum of 100 guests.<br>We can arrange the following for you:</p>
  <div class="service" style="left:132px">
    <div class="circle" role="img" aria-label="Photo of people holding candles at a vigil" style="background:radial-gradient(circle,#b0702a,#2a1a10)"></div>
    <h4>Vigil The Night Before<br>The Funeral</h4>
  </div>
  <div class="service" style="left:450px">
    <div class="circle" role="img" aria-label="Photo of a priest celebrating the eucharist" style="background:radial-gradient(circle,#e8dcc8,#8a7050)"></div>
    <h4>Eucharistic Celebration<br>With Priest</h4>
    <small>(on Tuesday and Friday in the parishes of<br>Heidewaarde)</small>
  </div>
  <div class="service" style="left:768px">
    <div class="circle" role="img" aria-label="Photo of priests leading a prayer service at an altar" style="background:radial-gradient(circle,#d08a60,#6a4a3a)"></div>
    <h4>Prayer Service With Priest</h4>
    <small>(if Possible)</small>
  </div>
</section>

<section class="cta" role="img" aria-label="Photo of a bouquet of white roses and lilac flowers">
  <div class="q">Do You Have Any Questions Or Would You<br>Like To Call In Our Funeral Home?</div>
  <div class="lead">Contact Us. We Are Here For You.</div>
  <a class="btn-outline btn-light" style="left:142px;top:212px;width:149px;height:40px;font-size:15px">Contact Us Today</a>
  <div class="call">Call Now : 013 58 20 40</div>
</section>

<section class="inquiry">
  <div class="inquiry-box">
    <h2>Quick Inquiry</h2>
    <div class="intro">Lorem ipsum dolor sit amet, consectetuer adipiscing elit, sed diam nonummy<br>nibh euismod tincidunt ut laoreet dolore.</div>
    <div class="field" style="left:47px;top:127px;width:271px;height:35px">First Name</div>
    <div class="field" style="left:332px;top:127px;width:271px;height:35px">Last Name</div>
    <div class="field" style="left:47px;top:176px;width:271px;height:35px">Email</div>
    <div class="field" style="left:332px;top:176px;width:271px;height:35px">Phone</div>
    <div class="field" style="left:47px;top:225px;width:556px;height:92px">Message</div>
    <a class="btn-outline btn-gold" style="left:264px;top:339px;width:122px;height:39px;font-size:14px">Submit Now</a>
    <svg class="corner" width="80" height="40" viewBox="0 0 80 40"><path d="M38 2L75 40H38z" fill="#dcdcdc"/><path d="M0 2h38v38z" fill="#a8840f"/></svg>
  </div>
</section>

<footer>
  <h5 style="left:142px">Quick Links</h5>
  <ul class="links">
    <li>Home</li><li>About us</li><li>Condole online</li><li>Order flowers</li><li>Contact</li>
  </ul>
  <h5 style="left:310px">Contact Details</h5>
  <div class="contact">
    <div class="row"><svg width="11" height="14" viewBox="0 0 12 16"><path d="M6 0a6 6 0 0 0-6 6c0 4 6 10 6 10s6-6 6-10a6 6 0 0 0-6-6zm0 8.5A2.5 2.5 0 1 1 6 3.5a2.5 2.5 0 0 1 0 5z" fill="#ddd"/></svg><div>Funeral Home Verhaegen<br>Kapelstraat 7, 3999 Lindeveld (Heidewaarde)</div></div>
    <div class="row"><svg width="12" height="12" viewBox="0 0 24 24"><path d="M5 2h4l2 5-2.5 1.5a11 11 0 0 0 6 6L16 12l5 2v4a2 2 0 0 1-2 2A16 16 0 0 1 3 4a2 2 0 0 1 2-2z" fill="#ddd"/></svg>013 58 20 40</div>
    <div class="row"><svg width="12" height="12" viewBox="0 0 24 24"><rect x="5" y="2" width="14" height="6" fill="none" stroke="#ddd" stroke-width="2"/><rect x="2" y="9" width="20" height="9" rx="1" fill="#ddd"/><rect x="6" y="15" width="12" height="7" fill="#1a1a1a" stroke="#ddd" stroke-width="2"/></svg>013 58 20 40</div>
    <div class="row" style="font-size:11.5px"><svg width="14" height="12" viewBox="0 0 24 20" fill="none" stroke="#ddd" stroke-width="2"><path d="M2 8l10-6 10 6v11H2z"/><path d="M2 8l10 6 10-6"/></svg>contact@verhaegen-rouw.example</div>
  </div>
  <h5 style="left:596px">Location Map</h5>
  <div class="map" role="img" aria-label="Street map showing the funeral home location in Heidewaarde"></div>
  <div class="foot-brand">
    <span class="brand-mark"></span>
    <div class="brand-name">Funeral home<br>Verhaegen <small>bvba</small></div>
  </div>
  <div class="social"><span></span><span></span><span></span><span></span></div>
</footer>

<div class="bottombar">
  <div class="copy">Copyright © 2019 Funeral Home Verhaegen. All Rights Reserved.</div>
  <div class="legal">Sitemap &nbsp;|&nbsp; Privacy Policy</div>
</div>

</body>
</html>
```